Hollins Pipework telephone book advert

Design a ringbook listings telephone book advertisement. Attached is a current version of the hollins pipework advert. Please use the same information as detailed on the existing advert but arty!. Overall size should be 130 mm by 91 mm portrait using one of the specified colours plus black. Any background should be opaque (not white). and delivered in the formats as specified.

```html
<!DOCTYPE html>
<html lang="en">
<head>
<meta charset="utf-8">
<title>Hollins Pipework – Directory Advert</title>
<link href="https://fonts.googleapis.com/css2?family=Raleway:wght@300;400;500;600;700;800;900&display=swap" rel="stylesheet">
<style>
  :root {
    --advert-yellow: #fff200;
    --ink: #000000;
    --backdrop: #e9e6df;
  }
  html, body {
    margin: 0;
    padding: 0;
    width: 1200px;
    height: 1200px;
    overflow: hidden;
    background: var(--backdrop);
  }
  .advert {
    position: absolute;
    left: 200px;
    top: 29px;
    width: 800px;
    height: 1142px;
    background: var(--advert-yellow);
    color: var(--ink);
    font-family: "Raleway", sans-serif;
    font-variant-numeric: lining-nums;
    font-feature-settings: "lnum" 1;
  }
  .line {
    position: absolute;
    left: 0;
    right: 0;
    text-align: center;
    transform: translateY(-50%);
    white-space: nowrap;
    line-height: 1;
  }
  .company-name { top: 98px; font-size: 60px; font-weight: 800; letter-spacing: 0.5px; }
  .company-suffix { top: 154px; font-size: 50px; font-weight: 300; letter-spacing: 24px; padding-left: 24px; }
  .call-prompt { top: 245px; font-size: 29px; font-weight: 700; }
  .phone-number { top: 336px; font-size: 124px; font-weight: 900; letter-spacing: 2px; }
  .survey-banner {
    top: 439px;
    display: flex;
    justify-content: center;
    align-items: center;
    gap: 12px;
    font-size: 29px;
  }
  .survey-banner strong { font-weight: 800; }
  .survey-banner span { font-weight: 500; }
  .house-icon { width: 88px; height: 76px; flex-shrink: 0; }

  .service-list {
    position: absolute;
    left: 76px;
    top: 516px;
    margin: 0;
    padding: 0;
    list-style: none;
  }
  .service {
    display: flex;
    align-items: center;
    height: 44.5px;
    white-space: nowrap;
  }
  .service-icon { width: 44px; height: 44px; margin-right: 22px; flex-shrink: 0; }
  .service-label { font-size: 23px; font-weight: 800; margin-right: 6px; }
  .service-detail { font-size: 18px; font-weight: 500; }

  .contact-role { top: 744px; font-size: 30px; font-weight: 500; }
  .contact-name { top: 808px; font-size: 66px; font-weight: 300; }
  .contact-name strong { font-weight: 800; }
  .contact-email {
    top: 874px;
    display: flex;
    justify-content: center;
    align-items: center;
    gap: 10px;
    font-size: 31px;
    font-weight: 500;
  }
  .email-icon { width: 40px; height: 28px; }
  .website {
    top: 976px;
    display: flex;
    justify-content: center;
    align-items: center;
    gap: 28px;
    font-size: 92px;
    font-weight: 600;
    letter-spacing: -1px;
  }
  .globe-icon { width: 105px; height: 110px; flex-shrink: 0; }
  .address { top: 1081px; font-size: 24px; font-weight: 500; }
</style>
</head>
<body>
<main class="advert">
  <div class="line company-name">HOLLINS PIPEWORK</div>
  <div class="line company-suffix">LIMITED</div>

  <div class="line call-prompt">FOR LOCAL DRAINAGE EXPERTISE CALL:</div>
  <div class="line phone-number">318-640</div>

  <div class="line survey-banner">
    <svg class="house-icon" viewBox="0 0 88 76" aria-hidden="true">
      <path d="M4 34 L44 5 L84 34" fill="none" stroke="#000" stroke-width="7"/>
      <path d="M15 29 V75 M73 29 V75" stroke="#000" stroke-width="7"/>
      <text x="44" y="70" text-anchor="middle" font-family="Raleway, sans-serif" font-weight="800" font-size="50">£</text>
    </svg>
    <div><strong>HOME BUYER</strong> <span>SURVEYS</span></div>
    <svg class="house-icon" viewBox="0 0 88 76" aria-hidden="true">
      <path d="M4 34 L44 5 L84 34" fill="none" stroke="#000" stroke-width="7"/>
      <path d="M15 29 V75 M73 29 V75" stroke="#000" stroke-width="7"/>
      <text x="44" y="70" text-anchor="middle" font-family="Raleway, sans-serif" font-weight="800" font-size="50">£</text>
    </svg>
  </div>

  <ul class="service-list">
    <li class="service">
      <svg class="service-icon" viewBox="0 0 44 44" aria-hidden="true">
        <path d="M9 12 C4 16 5 24 12 31 C19 38 27 40 31 35 L33 32 L26 26 L22 29 C19 28 16 25 15 22 L18 18 L12 11 Z" fill="#000"/>
        <circle cx="32" cy="11" r="9" fill="#000"/>
        <path d="M32 6.5 V15.5 M27.5 11 H36.5" stroke="#fff200" stroke-width="2.6"/>
      </svg>
      <span class="service-label">Emergencies:</span>
      <span class="service-detail">Unblocking and high pressure cleaning</span>
    </li>
    <li class="service">
      <svg class="service-icon" viewBox="0 0 44 44" aria-hidden="true">
        <path d="M10 10 L36 37" stroke="#000" stroke-width="6" stroke-linecap="round"/>
        <path d="M34 8 L9 34" stroke="#000" stroke-width="6" stroke-linecap="round"/>
        <circle cx="9" cy="9" r="6.5" fill="#000"/>
        <circle cx="9" cy="9" r="2.5" fill="#fff200"/>
        <circle cx="8" cy="36" r="5" fill="#000"/>
        <path d="M31 5 L38 4 L39 11 L35 13 Z" fill="#000"/>
      </svg>
      <span class="service-label">Mainteinance:</span>
      <span class="service-detail">Jetting, de-scaling &amp; root cutting</span>
    </li>
    <li class="service">
      <svg class="service-icon" viewBox="0 0 44 44" aria-hidden="true">
        <g transform="rotate(25 26 17)">
          <rect x="12" y="11" width="26" height="12" rx="2" fill="#000"/>
          <rect x="38" y="13" width="4" height="8" fill="#000"/>
        </g>
        <path d="M20 25 L16 31 H8" fill="none" stroke="#000" stroke-width="4"/>
        <path d="M5 24 V38" stroke="#000" stroke-width="4"/>
      </svg>
      <span class="service-label">Survey:</span>
      <span class="service-detail">Modern CCTV, condition reports</span>
    </li>
    <li class="service">
      <svg class="service-icon" viewBox="0 0 44 44" aria-hidden="true">
        <path d="M16 3 H26 V8 H16 Z" fill="#000"/>
        <path d="M17 9 H25 V16 L31 24 L25 28 L21 22 V34 H13 V20 L17 16 Z" fill="#000"/>
        <rect x="10" y="34" width="14" height="5" fill="#000"/>
        <path d="M33 30 C30 35 30 38 33 38 C36 38 36 35 33 30 Z" fill="#000"/>
      </svg>
      <span class="service-label">Rehabilitation:</span>
      <span class="service-detail">Structural re-lining of damaged and leaky drains</span>
    </li>
  </ul>

  <div class="line contact-role">CONTRACTS MANAGER</div>
  <div class="line contact-name">OWEN <strong>TRESSIDER</strong></div>
  <div class="line contact-email">
    <svg class="email-icon" viewBox="0 0 40 28" aria-hidden="true">
      <rect x="2" y="2" width="36" height="24" fill="none" stroke="#000" stroke-width="2.5"/>
      <path d="M2 2 L20 16 L38 2 M2 26 L15 12 M38 26 L25 12" fill="none" stroke="#000" stroke-width="2.5"/>
    </svg>
    <span>office@hpw.gg</span>
  </div>

  <div class="line website">
    <svg class="globe-icon" viewBox="0 0 105 110" aria-hidden="true">
      <circle cx="50" cy="52" r="44" fill="none" stroke="#000" stroke-width="9"/>
      <ellipse cx="50" cy="52" rx="18" ry="44" fill="none" stroke="#000" stroke-width="8"/>
      <path d="M8 38 H92 M8 66 H70" stroke="#000" stroke-width="8"/>
      <path d="M62 62 L100 82 L84 86 L94 104 L86 108 L76 90 L64 100 Z" fill="#000" stroke="#fff200" stroke-width="4"/>
    </svg>
    <span>www.hpw.gg</span>
  </div>

  <div class="line address">Les Coutures Lane, Vale, Guernsey GY3 5XQ</div>
</main>
</body>
</html>
```